Buchcover-Design für Buch der Schleier-Biografie gesucht
Zielgruppe
Das Genre nennt sich Schleier-Biografie. Typischerweise sind es Leserinnen, die sich vom fremden Schicksal berühren lassen wollen. Die Bücher stellen Unterdrückung und Gewalt gegen Frauen dar, aber immer auch eine Befreiung.
Einige typische Cover habe ich beigefügt. Wichtig ist, dass die Autorin anonym bleiben will.
Aufgabenstellung
Autoren:
Jonas Kolbwetter
Dilan K.
Ich benötige ein deutsches und ein englisches Cover:
Titel: Die stille Mauer
Untertitel: Wie ich mein Zuhause verließ und neu anfing
Titel: The Quiet Wall
Untertitel: How I left my home and found a new start
Dies wird der Text bei Buchplatz sein:
“Talaq”, sagte er, als lese er aus seinem arabischen Buch vor. “Frau, ich verstoße dich.”
Meine Mutter sah auf. Ihre großen Augen lagen in seinem Blick. Meine schöne Mutter, ihr Gesicht ganz bleich.
“Talaq”, sagte er wieder. “Ich verstoße dich, Sirwe.”
“Nein”, flüsterte sie. “Das kannst du nicht tun. Die Kinder - “
“Talaq, du bist verstoßen. Verlasse mein Haus, verlasse deine Kinder.”
Ich bin Dilan. - Am Anfang des Buches komme ich in den Kindergarten, eine kleine Kurdin aus Erbil im Nordirak. Mein Vater ist alt und strenggläubig, meine Mutter ist jung und hübsch. Als er die Scheidung gegen sie ausspricht - das dreimalige Talaq - muss sie ohne ihre Kinder das Haus verlassen. So ist es üblich im Islam, denn die Kinder gehören dem Mann.
Wo mein Leben in meiner Erinnerung anfängt, beginnt es wie ein deutsches Märchen. So viel habe ich in dem Märchen Aschenputtel von mir gefunden, dass ich denke, mein kurdisches Leben ist nichts anders als ein deutsches Märchen, das man den Kindern erzählt, damit sie sich fürchten.
Also handelt dieses Buch von einem Mädchen, das in die Finsternis und in den Schmutz gestoßen wird. Und doch bin ich ein Mädchen von Millionen, denn dort wo ich herkomme, ist jedes Mädchen ein Aschenputtel. Das glückliche Ende des Märchens - davon träumen sie vergeblich. Und ihr Märchenprinz - das ist ein Mann, der sie nicht schlägt.
Ich werde erzählen, wie ich versucht habe, meinen Vater und seinen Gott zu verstehen. Es macht mir ein wenig Angst, darüber zu schreiben – das sollten Sie wissen. In diesem Buch ist deshalb alles ..

```html
<!DOCTYPE html>
<html lang="de">
<head>
<meta charset="utf-8">
<title>Die stille Mauer – Buchcover</title>
<link href="https://fonts.googleapis.com/css2?family=Dawning+of+a+New+Day&family=Jost:wght@400&display=swap" rel="stylesheet">
<style>
  :root {
    --stage: #ececec;
    --ink-light: #ffffff;
    --cover-black: #050505;
    --gold: #b8913c;
    --gold-deep: #a67f2e;
    --veil-brown: #3d3330;
    --script: "Dawning of a New Day", cursive;
    --sans: "Jost", sans-serif;
  }
  * { box-sizing: border-box; margin: 0; padding: 0; }
  html, body { width: 1200px; height: 802px; overflow: hidden; background: var(--stage); }
  .stage { position: relative; width: 1200px; height: 802px; }

  /* Front cover */
  .front-cover {
    position: absolute; left: 55px; top: 51px; width: 470px; height: 700px;
    overflow: hidden; background: var(--cover-black);
  }
  .front-photo {
    position: absolute; inset: 0;
    background:
      linear-gradient(180deg, #060606 0%, #060606 28%, #6d5446 34%, #b08b78 38%, #1a1614 44%, #050505 52%, #050505 100%),
      var(--cover-black);
  }
  .front-title {
    position: absolute; left: 36px; top: 560px; width: 420px;
    color: var(--ink-light);
  }
  .front-title .title {
    font-family: var(--script); font-weight: 400; font-size: 46px; line-height: 1;
    transform: rotate(3deg); transform-origin: left center;
  }
  .front-title .subtitle {
    margin: 6px 0 0 60px;
    font-family: var(--sans); font-size: 12px; letter-spacing: .2px;
    transform: rotate(3deg); transform-origin: left center;
  }

  /* Back cover */
  .back-cover {
    position: absolute; left: 610px; top: 51px; width: 470px; height: 700px;
    overflow: hidden;
  }
  .back-photo {
    position: absolute; inset: 0;
    background: linear-gradient(160deg, #d9d6da 0%, #c9c3cc 30%, #9d9a9a 55%, #c4bca8 75%, #6f6f68 100%);
  }
  .veil-icon {
    position: absolute; left: 20px; top: 40px; width: 90px; height: 165px;
    background: var(--veil-brown); border-radius: 45px 45px 30px 40px; z-index: 2;
  }
  .blurb-panel {
    position: absolute; left: 70px; top: 100px; width: 312px; height: 545px;
    background: var(--gold); color: var(--ink-light);
    padding: 18px 14px 14px 14px;
    font-family: var(--sans); font-size: 10.6px; line-height: 1.32;
    text-align: justify;
  }
  .blurb-panel p + p { margin-top: 5px; }
  .blurb-panel .lead { margin-left: 46px; }
  .blurb-panel .quote { margin-top: 28px; text-align: left; }

  /* Spine */
  .spine {
    position: absolute; left: 1080px; top: 51px; width: 62px; height: 700px;
    background: linear-gradient(90deg, var(--gold-deep), var(--gold) 40%, var(--gold-deep));
    display: flex; align-items: flex-start; justify-content: center; padding-top: 120px;
    color: var(--ink-light);
  }
  .spine-text { writing-mode: vertical-rl; display: flex; flex-direction: row-reverse; gap: 2px; align-items: flex-start; }
  .spine .title { font-family: var(--script); font-size: 34px; line-height: 1; }
  .spine .subtitle { font-family: var(--sans); font-size: 8.5px; margin-top: 12px; }
</style>
</head>
<body>
<main class="stage">
  <section class="front-cover">
    <div class="front-photo" role="img" aria-label="Foto: Gesicht einer Frau im schwarzen Niqab, nur die Augen sichtbar"></div>
    <div class="front-title">
      <h1 class="title">Die stille Mauer</h1>
      <p class="subtitle">Wie ich mein Zuhause verließ und neu anfing</p>
    </div>
  </section>

  <section class="back-cover">
    <div class="back-photo" role="img" aria-label="Unscharfes Hintergrundfoto in Grau- und Lilatönen"></div>
    <div class="veil-icon" role="img" aria-label="Illustration: Kopftuch-Silhouette"></div>
    <div class="blurb-panel">
      <p class="lead">Ich bin Dilan. - Am Anfang des Buches komme ich in den Kindergarten, eine kleine Kurdin aus Erbil im Nordirak. Mein Vater alt und strenggläubig, meine Mutter ist jung und hübsch. Als er die Scheidung gegen sie ausspricht, muss sie ohne ihre Kinder das Haus verlassen. So ist es üblich im Islam, denn die Kinder gehören dem Mann.</p>
      <p>Wo mein Leben in meiner Erinnerung anfängt, beginnt es wie ein deutsches Märchen. So viel habe ich in dem Märchen Aschenputtel von mir gefunden, dass ich denke, mein kurdisches Leben ist nicht anders als ein deutsches Märchen, das man den Kindern erzählt, damit sie sich fürchten.</p>
      <p>Also handelt dieses Buch von einem Mädchen, das in die Finsternis und den Schmutz gestoßen wird. Und doch bin ich ein Mädchen von Millionen, denn dort wo ich herkomme, ist jedes Mädchen ein Aschenputtel. Das glückliche Ende des Märchens - davon träumen sie vergeblich. Und ihr Märchenprinz - das ist ein Mann, der sie nicht schlägt.</p>
      <p>Ich werde erzählen, wie ich versucht habe, meinen Vater zu verstehen. Und weil es mir nicht gelang, habe ich versucht, seinen Gott zu verstehen. Ich habe ein wenig Angst, darüber zu schreiben – das sollten Sie wissen. In diesem Buch ist deshalb alles von mir, nur mein Name fehlt.</p>
      <p class="quote">“Talaq”, sagte er. “Ich verstoße dich, Sirwe.”<br>“Nein”, flüsterte meine Mutter. “Das kannst du nicht tun. Die Kinder - ”<br>“Talaq, du bist verstoßen.<br>Verlasse mein Haus, verlasse deine Kinder.”</p>
    </div>
  </section>

  <aside class="spine">
    <div class="spine-text">
      <span class="title">Die stille Mauer</span>
      <span class="subtitle">Wie ich mein Zuhause verließ und neu anfing</span>
    </div>
  </aside>
</main>
</body>
</html>
```